Buchverlag sucht Cover-Design
Zielgruppe
Wir sind ein Buchverlag, der über Bravolo publizieren.
Unsere Zielgruppe sind: alle Selbstständigen, Unternehmern, Intrapreneuren, genauso wie Coaches, Experten, Start-ups und Entrepreneure.
Auch an diejenigen, die dieses Vorhaben angehen möchten.
Aufgabenstellung
Das Cover soll Nischen entsprechend sein. (Business Findung und Gestaltung)
Andersartig, auffallend, jedoch seriös sein.
Genaue Vorstellung:
Ein im freien Naturlandschaft fliegender Adler, der seine Beute fest im Blick hat und zielgenau seine Beute
zugreifen kann!
Den Schriftzug auffällig gestalten
Titel:
HOHE WARTE - Echter Reichtum gehört jedem von Anfang an
Untertitel:
Die klare Haltung der Vorreiter mit praktischem Wegweiser für Klarheit & Zufriedenheit bei privaten und beruflichen Weichenstellungen
Autor:
Velina Korbach
Logo des Verlags im Anhang
Name des Verlags:
Mond Quelle Verlag

```html
<!DOCTYPE html>
<html lang="de">
<head>
<meta charset="utf-8">
<title>Hohe Warte – Velina Korbach</title>
<link rel="stylesheet" href="https://fonts.googleapis.com/css2?family=Playfair+Display:wght@400&family=Signika:wght@500;600&display=swap">
<style>
  :root {
    --sky-deep: #237b8f;
    --sky-mid: #7eaebe;
    --sky-pale: #c9d6dd;
    --white: #ffffff;
    --accent: #f8bb3f;
  }
  html, body {
    margin: 0;
    padding: 0;
    width: 848px;
    height: 1200px;
    overflow: hidden;
  }
  .cover {
    position: relative;
    width: 848px;
    height: 1200px;
    overflow: hidden;
    font-family: "Signika", "Source Sans 3", sans-serif;
    color: var(--white);
  }
  .cover-photo {
    position: absolute;
    inset: 0;
    background:
      radial-gradient(ellipse at 100% 100%, var(--sky-pale) 0%, rgba(201,214,221,0) 60%),
      linear-gradient(160deg, var(--sky-deep) 0%, #4a92a6 30%, var(--sky-mid) 55%, #a9c2cc 80%, var(--sky-pale) 100%);
  }
  .author {
    position: absolute;
    left: 45px;
    top: 26px;
    margin: 0;
    font-size: 38px;
    font-weight: 600;
    color: var(--accent);
    letter-spacing: 0.2px;
  }
  .title {
    position: absolute;
    left: 44px;
    top: 62px;
    margin: 0;
    font-family: "Playfair Display", "Times New Roman", serif;
    font-weight: 400;
    font-size: 186px;
    line-height: 158px;
    letter-spacing: -2px;
  }
  .title span { display: block; }
  .tagline {
    position: absolute;
    left: 52px;
    top: 404px;
    margin: 0;
    font-size: 33px;
    font-weight: 500;
    letter-spacing: -0.3px;
  }
  .subtitle {
    position: absolute;
    left: 52px;
    top: 942px;
    width: 770px;
    margin: 0;
    font-size: 37px;
    font-weight: 500;
    line-height: 49px;
    letter-spacing: -0.3px;
  }
  .publisher {
    position: absolute;
    left: 0;
    right: 0;
    top: 1122px;
    display: flex;
    justify-content: center;
    align-items: center;
    gap: 10px;
  }
  .publisher-name {
    font-size: 50px;
    font-weight: 600;
    color: var(--accent);
    line-height: 1;
  }
</style>
</head>
<body>
  <main class="cover">
    <div class="cover-photo" role="img" aria-label="Foto: weiter blaugrauer Himmel mit einem einzelnen fliegenden Vogel in der Bildmitte"></div>

    <p class="author">Velina Korbach</p>

    <h1 class="title"><span>HOHE</span><span>WARTE</span></h1>

    <p class="tagline">Echter Reichtum gehört jedem von Anfang an</p>

    <p class="subtitle">Die klare Haltung der Vorreiter mit praktischem Wegweiser für Klarheit &amp; Zufriedenheit bei privaten und beruflichen Weichenstellungen</p>

    <div class="publisher" aria-label="Mond Quelle Verlag">
      <svg width="30" height="30" viewBox="0 0 30 30" aria-hidden="true">
        <circle cx="15" cy="15" r="13" fill="var(--accent)"/>
      </svg>
      <span class="publisher-name">MQV</span>
    </div>
  </main>
</body>
</html>
```